Digitales Briefpapier für IT-Systemhaus
Zielgruppe
IT-Systemhaus mit dem Schwerpunkt Digitalisierung von Geschäftsprozessen. Ggf. Schlagwörter wie DMS, ECM, Digitalisierung Ihrer Prozesse unterbringen.
Aufgabenstellung
Digitale Vorlage (Word) um daraus dann ein PDF zu generieren. Anschrift usw. auf QXR.de

```html
<!DOCTYPE html>
<html lang="de">
<head>
<meta charset="utf-8">
<title>QXR.de Briefpapier</title>
<link rel="stylesheet" href="https://fonts.googleapis.com/css2?family=Open+Sans:wght@400;600&display=swap">
<style>
:root{
  --backdrop:#9b9b9b;
  --paper:#ffffff;
  --navy:#25375a;
  --blue:#2f60a9;
  --ink:#3a3a3a;
  --light:#e4e8ef;
}
*{margin:0;padding:0;box-sizing:border-box}
html,body{width:847px;height:1200px;overflow:hidden;background:var(--backdrop)}
body{font-family:"Open Sans",Arial,sans-serif;position:relative}
.sheet{position:absolute;left:53px;top:76px;width:741px;height:1047px;background:var(--paper)}
.masthead{position:absolute;left:0;top:0;width:741px;height:100px;background:var(--navy)}
.brand{position:absolute;left:70px;top:32px;font-weight:600;font-size:28px;color:var(--light);line-height:36px}
.company{position:absolute;left:349px;top:34px;font-size:8.6px;line-height:12.6px;color:var(--light)}
.company .name{color:var(--blue);font-weight:600}
.contact{position:absolute;left:589px;top:25px;font-size:8.6px;line-height:13.9px;color:var(--light);list-style:none}
.contact b{color:var(--blue);font-weight:600;margin-right:4px}
.return-line{position:absolute;left:107px;top:157px;font-size:6px;line-height:9px;color:var(--ink);border-bottom:0.8px solid var(--ink);white-space:nowrap}
.return-line .name{color:var(--blue)}
.return-line .sep{color:#999;margin:0 4px}
.fold-mark{position:absolute;left:26px;width:6px;height:8px}
.fold-mark.first{top:390px}
.fold-mark.second{top:665px}
.legal{position:absolute;left:69px;top:971px;font-size:8.6px;line-height:13.6px;color:var(--ink)}
.rule{position:absolute;top:994px;height:10px;background:var(--blue)}
.rule.left{left:0;width:53px}
.rule.right{left:229px;width:512px}
.tagline{position:absolute;right:36px;top:1010px;font-size:12.5px;line-height:17px;color:var(--blue);white-space:nowrap}
</style>
</head>
<body>
<main class="sheet">
  <header class="masthead">
    <div class="brand">QXR.de</div>
    <div class="company">
      <div class="name">QXR.de Systemhaus GmbH &amp; Co. KG</div>
      <div>Fennweg 42b</div>
      <div>31999 Halmstedt</div>
    </div>
    <ul class="contact">
      <li><b>T.</b>+49 (555) 4081720</li>
      <li><b>F.</b>+49 (555) 40817299</li>
      <li><b>E.</b>info(at)qxr.de</li>
      <li><b>W.</b>www.qxr.de</li>
    </ul>
  </header>

  <div class="return-line"><span class="name">QXR.de Systemhaus GmbH &amp; Co. KG</span><span class="sep">|</span>Fennweg 42b<span class="sep">|</span>31999 Halmstedt</div>

  <svg class="fold-mark first" viewBox="0 0 6 8"><polygon points="0,0 6,4 0,8" fill="var(--blue)"/></svg>
  <svg class="fold-mark second" viewBox="0 0 6 8"><polygon points="0,0 6,4 0,8" fill="var(--blue)"/></svg>

  <footer>
    <div class="legal">
      <div>Amtsgericht Kellingen</div>
      <div>IBAN DE00 1234 5678 9012 3456 78</div>
      <div>BIC QXRBDE21XXX</div>
      <div>Ust. ID: DE000111222</div>
    </div>
    <div class="rule left"></div>
    <div class="rule right"></div>
    <div class="tagline">DMS, ECM, Digitalisierung Ihrer Prozesse unterbringen.</div>
  </footer>
</main>
</body>
</html>
```